Training company needs a Quick Reference Card design

We have draft skeleton of the design and most of the text. But we need a designer to take it the rest if the way.
I have designed a 2 page quick reference card - it is meant to be a 2-sided document. The first page is portrait, the back page can either be portrait or landscape, I'm not too concerned, whichever fits best.
Section called 'Maps' on front, a map is a collection of documents (like a manual), a topic is a document (like a page or section of a manual) and a block is a section of a document. The graphic is mean to illustrate the hierarchy but essentially a map is a big document with smaller documents in it.
Please use the company's logo colors to differentiate the different sections with minimal/ highlight only use of the darkest color, preferably.
Please use the icons for the corresponding Information types in the chart of the back - except please re-design the icons color scheme to match the company's logo/website colors.

Target Market(s)

Technical writers, after attending our training course, as an ongoing resource for them

Industry/Entity Type

It Company

Font styles to use
Sans Serif

Requirements
Must have
• Must adhere to look and feel of brand/ website. www.lumenrivet.com
Nice to have
• Please keep the design modern and slick looking, not too busy, easy to read

```html
<!DOCTYPE html>
<html lang="en">
<head>
<meta charset="utf-8">
<title>Quick Reference Card</title>
<link href="https://fonts.googleapis.com/css2?family=Lato:wght@400;700&family=Lexend:wght@600&display=swap" rel="stylesheet">
<style>
:root{
  --cyan:#1aa3cf;
  --cyan-light:#5bc2e2;
  --navy:#1c2b86;
  --teal-dark:#0f4a60;
  --pill-dark:#123f57;
  --ink:#2a2a2a;
  --paper:#ffffff;
  --bg:#d9dde0;
}
*{box-sizing:border-box;margin:0;padding:0}
html,body{width:1200px;height:1200px;overflow:hidden;background:var(--bg)}
body{font-family:"Lato",Arial,sans-serif;color:var(--ink)}
.stage{position:absolute;left:0;top:0;width:1500px;height:1500px;transform:scale(.8);transform-origin:0 0}
.card{position:absolute;background:var(--paper)}
.card::after{content:"";position:absolute;left:0;right:0;bottom:0;height:9px;background:var(--teal-dark)}
.abs{position:absolute}

/* front */
.front{left:84px;top:378px;width:564px;height:797px}
.brand{left:22px;top:25px;display:flex;align-items:center;gap:10px}
.brand-dot{width:50px;height:50px;border-radius:50%;background:var(--cyan)}
.brand-name{font-weight:700;font-size:17px;color:var(--navy)}
.title{left:252px;top:30px;font-family:"Lexend",Arial,sans-serif;font-size:26px;color:var(--navy)}
.box{position:absolute;border:2px solid var(--cyan)}
.map-title{position:absolute;top:6px;width:100%;text-align:center;color:var(--cyan);font-weight:700;font-size:18px}
.topic{position:absolute;top:36px;width:94px;height:107px;border:2px solid var(--cyan);text-align:center}
.topic h3{font-size:15px;margin-top:12px}
.pill{display:inline-block;background:var(--cyan);color:#fff;border-radius:9px;font-size:9px;padding:2px 6px;box-shadow:0 1px 2px rgba(0,0,0,.4)}
.topic .pill{position:absolute;left:50%;transform:translateX(-50%);white-space:nowrap}
.note{font-size:8.5px;line-height:1.3;padding:5px 10px;text-align:justify}
.section-title{position:absolute;top:2px;width:100%;text-align:center;font-size:16px}
.rule{position:absolute;top:30px;width:146px;height:118px;border:2px solid var(--cyan);text-align:center}
.rule .pill-dark{display:inline-block;margin-top:8px;background:var(--pill-dark);color:#fff;border-radius:10px;font-size:11px;padding:3px 10px}
.rule p{font-size:8.5px;line-height:1.3;text-align:justify;padding:6px 10px 0}
.panel{position:absolute;box-shadow:0 1px 4px rgba(0,0,0,.25);padding:18px 12px}
.panel h4{font-size:10.5px;font-weight:400;margin-bottom:26px}
.panel ol{font-size:11px;line-height:1.25;padding-left:18px}
.panel .blue{color:var(--cyan);font-size:11px;line-height:1.25}
.cog{left:22px;top:620px;width:518px;height:155px;border:2px solid var(--navy)}
.cog .section-title{top:6px}
.cog-item{position:absolute;top:34px;width:122px;height:112px;border:1.5px solid var(--navy);text-align:center}
.cog-item h5{font-size:13px;font-weight:400;margin-top:8px;margin-bottom:10px}
.cog-item p{font-size:8.5px;line-height:1.3;text-align:justify;padding:0 2px}
.cog-item p.cyan{color:var(--navy)}

/* back */
.back{left:668px;top:514px;width:747px;height:526px}
.grid{position:absolute;left:12px;top:14px;width:723px;height:500px;display:grid;
  grid-template-columns:98px 126px 122px 132px 126px 119px;
  grid-template-rows:22px 64px 108px 98px 40px 104px 64px;
  border:1.5px solid var(--cyan)}
.cell{border-right:1.5px solid var(--cyan);border-bottom:1.5px solid var(--cyan);font-size:8px;line-height:1.3;padding:12px 10px}
.cell:nth-child(6n){border-right:none}
.grid .cell:nth-last-child(-n+6){border-bottom:none}
.head{font-size:12px;text-align:center;padding:3px 0}
.center{display:flex;align-items:center;justify-content:center;font-size:10.5px;padding:0}
.label{display:flex;align-items:center;justify-content:center;padding:0 8px}
.label span{display:block;width:100%;background:var(--cyan);color:#fff;font-weight:700;font-size:12px;line-height:1.2;text-align:center;border-radius:7px;padding:6px 4px;box-shadow:0 1px 3px rgba(0,0,0,.35)}
</style>
</head>
<body>
<div class="stage">

<section class="card front">
  <div class="abs brand"><span class="brand-dot"></span><span class="brand-name">Lumen Rivet</span></div>
  <h1 class="abs title">Quick Reference Card</h1>

  <div class="box" style="left:20px;top:101px;width:232px;height:160px">
    <div class="map-title">MAP</div>
    <div class="topic" style="left:14px"><h3>Topic</h3><span class="pill" style="top:48px">Primary Block</span><span class="pill" style="top:76px">Sub-Block</span></div>
    <div class="topic" style="left:120px"><h3>Topic</h3><span class="pill" style="top:48px">Primary Block</span><span class="pill" style="top:76px">Sub-Block</span></div>
  </div>
  <div class="box note" style="left:264px;top:101px;width:278px;height:50px">A map is a file that organizes topics into structured collections of information. Maps specify hierarchy and relationships among topics</div>
  <div class="box note" style="left:264px;top:155px;width:278px;height:50px;padding-top:9px">A topic is a group of related blocks with a title. Use the chunking principle to group together relevant blocks</div>
  <div class="box note" style="left:264px;top:209px;width:278px;height:52px">A block is a bite-sized chunk of information about one main idea that allows the writer to organize the material into logical sections.</div>

  <div class="box" style="left:22px;top:277px;width:520px;height:162px">
    <div class="section-title">General writing rules</div>
    <div class="rule" style="left:12px"><span class="pill-dark">Effective sentences</span><p>One main agent, action &amp; outcome. Use active voice and simplest tense possible. No more than 7 sentences per paragraph. Use lists and tables</p></div>
    <div class="rule" style="left:182px"><span class="pill-dark">Special characters</span><p>Avoid special characters, spell out words instead. Remove parentheses, colons and dashes. Avoid using quotation marks and slashes.</p></div>
    <div class="rule" style="left:350px"><span class="pill-dark">Plain language</span><p>Write in short sentences. Provide useful titles. Use clear familiar words. Avoid excess words. Be consistent</p></div>
  </div>

  <div class="panel" style="left:22px;top:457px;width:300px;height:147px">
    <h4>3 Questions to ask before you start writing:</h4>
    <ol><li>What is the purpose of this information?</li><li>What is the desired user response of this information?</li><li>Who is the audience?</li><li>What is the purpose of this information?</li><li>What is the desired user response of this information?</li></ol>
  </div>
  <div class="panel" style="left:340px;top:457px;width:200px;height:147px">
    <h4>2 Types of language arts</h4>
    <p class="blue">LAFI – Language arts for information</p>
    <p class="blue">LAFPR – language arts for personal response</p>
  </div>

  <div class="abs cog">
    <div class="section-title">4 Cognitive Principles</div>
    <div class="cog-item" style="left:4px"><h5>Consistency</h5><p class="cyan">Use similar terms and structures. Pick a term and stick with it. Use the same sequence of blocks. Use</p></div>
    <div class="cog-item" style="left:131px"><h5>Chunking</h5><p class="cyan">Maximum of nine (7 +/- 2) items in a list, rows in a table, blocks in a topic, or topics in a map</p></div>
    <div class="cog-item" style="left:261px"><h5>Relevance</h5><p class="cyan">Group similar items together. Separate relevance? Separate block. Irrelevant? Delete it.</p></div>
    <div class="cog-item" style="left:388px"><h5>Titling</h5><p class="cyan">Name everything. Name every block, every topic, every map and every table column</p></div>
  </div>
</section>

<section class="card back">
  <div class="grid">
    <div class="cell"></div><div class="cell head">Reference</div><div class="cell head">Concept</div><div class="cell head">Principle</div><div class="cell head">Process</div><div class="cell head">Task</div>

    <div class="cell label"><span>Definition</span></div>
    <div class="cell">Describes things the reader needs to know</div>
    <div class="cell">Explains things the reader needs to understand</div>
    <div class="cell">Advises the reader what they need to do or not do and when</div>
    <div class="cell">Demonstrates to the reader how things work</div>
    <div class="cell">Instructs the reader on how to do things</div>

    <div class="cell label"><span>Types of authoring models</span></div>
    <div class="cell">Sentences/phrases<br>Lists (ol, ul)<br>Tables<br>Diagrams<br>Part-description<br>Part-function</div>
    <div class="cell">Sentences/phrases<br>Lists (ol, ul)<br>Tables<br>Illustrations</div>
    <div class="cell">Sentences/phrases<br>Lists (ol, ul)<br>Tables<br>Decision tree<br>Graphic</div>
    <div class="cell">Sentences/phrases<br>Stage ordered list<br>When/then condition tree<br>Graphic example</div>
    <div class="cell">Sentences/phrases<br>Lists<br>If/then decision tree<br>Graphic example</div>

    <div class="cell label"><span>Titling best practices</span></div>
    <div class="cell">Describes the item and anything that differentiates it from other items</div>
    <div class="cell">Use the plural form of the noun, if one exists. Don't add additional words such as "About", "What is", or "Definition"</div>
    <div class="cell">Identifies the principle and expresses the gravity of the principle. Formula= gravity + principle, or principle + gravity</div>
    <div class="cell">Human processes: Gerund of verb + noun "Grooming a dog".<br>System processes: Use "How (item) works" Ex "How engines work"</div>
    <div class="cell">Starts with an imperative verb, do not use gerund.<br>"Mow the lawn"<br>"Boil and egg"<br>"Register for a course"</div>

    <div class="cell label"><span>Primary block title</span></div>
    <div class="cell center">Introduction</div><div class="cell center">Definition</div><div class="cell center">Statement</div><div class="cell center">Summary</div><div class="cell center">Purpose</div>

    <div class="cell label"><span>Primary block content</span></div>
    <div class="cell">Provide a description of the reference topic and how it would be used</div>
    <div class="cell">Provide the exact meaning of the concept</div>
    <div class="cell">Provide a high-level summary of the principle</div>
    <div class="cell">Provide a short explanation of the purpose of the process, or the need for the process</div>
    <div class="cell">Provide an explanation of why or when the reader would use the task</div>

    <div class="cell label"><span>Tips and examples</span></div>
    <div class="cell"></div><div class="cell"></div><div class="cell"></div><div class="cell"></div><div class="cell"></div>
  </div>
</section>

</div>
</body>
</html>
```